Crestmoor Valor Cleaning Solutions

Need a logo and business card design. I want to use a translucent business card. I want to abbreviate the name C.V.C.S. Commercial Cleaning, because my is Tam. I’d also like to incorporate a knight or something like that. I want the idea to tie in with the word Crestmoor. New ideas are welcome, i don’t want to limit anyone’s creativity.

Target Market(s)

Commercial Cleaning for businesses.

Contact Information for Business Card

Crestmoor
Valor
Cleaning
Solutions

```html
<!DOCTYPE html>
<html lang="en">
<head>
<meta charset="utf-8">
<title>Crestmoor Valor Cleaning Solutions – Business Card</title>
<link href="https://fonts.googleapis.com/css2?family=Arimo:ital,wght@0,400;0,700;1,700&display=swap" rel="stylesheet">
<style>
  :root {
    --stage: #d9dde2;
    --card-frost: #eef2f6;
    --navy: #14132e;
    --gold: #8c7f34;
    --ink: #1c1c24;
  }
  html, body {
    margin: 0;
    width: 1200px;
    height: 970px;
    overflow: hidden;
    background: var(--stage);
  }
  .canvas {
    position: relative;
    width: 1200px;
    height: 970px;
  }
  .business-card {
    position: absolute;
    left: 80px;
    top: 187px;
    width: 1040px;
    height: 594px;
    background: linear-gradient(180deg, #f4f6f9 0%, var(--card-frost) 60%, #e6ebf1 100%);
    font-family: "Arimo", Arial, sans-serif;
    color: var(--ink);
    box-shadow: 0 6px 24px rgba(20, 19, 46, 0.15);
  }
  .brand {
    position: absolute;
    left: 148px;
    top: 95px;
    width: 744px;
    height: 165px;
    display: flex;
    align-items: center;
    gap: 34px;
  }
  .brand-dot {
    flex: 0 0 auto;
    width: 120px;
    height: 120px;
  }
  .brand-name {
    margin: 0;
    color: var(--navy);
    font-size: 54px;
    font-weight: 700;
    line-height: 1.12;
  }
  .brand-name span { display: block; }
  .name-rule {
    position: absolute;
    left: 0;
    right: 0;
    top: 344px;
    display: flex;
    align-items: center;
    gap: 10px;
  }
  .name-rule .rule {
    flex: 1;
    height: 4px;
    background: var(--gold);
  }
  .name-rule .rule.left { flex: 0 0 390px; }
  .person-name {
    font-size: 33px;
    font-weight: 700;
    color: var(--navy);
    letter-spacing: 0.5px;
  }
  .contact {
    position: absolute;
    left: 0;
    right: 0;
    top: 423px;
    text-align: center;
    font-size: 25px;
    line-height: 34px;
  }
  .contact p { margin: 0; }
  .label {
    color: var(--gold);
    font-weight: 700;
    font-style: italic;
  }
  .web { letter-spacing: 2px; }
  .web .domain {
    color: var(--gold);
    font-weight: 700;
    font-style: italic;
  }
  .base-band {
    position: absolute;
    left: 0;
    right: 0;
    bottom: 0;
    height: 22px;
    background: var(--navy);
  }
</style>
</head>
<body>
<div class="canvas">
  <section class="business-card">
    <div class="brand">
      <svg class="brand-dot" viewBox="0 0 120 120" aria-hidden="true">
        <circle cx="60" cy="60" r="58" fill="var(--navy)"/>
      </svg>
      <h1 class="brand-name"><span>Crestmoor Valor</span><span>Cleaning Solutions</span></h1>
    </div>

    <div class="name-rule">
      <span class="rule left"></span>
      <span class="person-name">ROWAN HALE</span>
      <span class="rule"></span>
    </div>

    <div class="contact">
      <p><span class="label">P:</span> (555) 013-2468 | <span class="label">E:</span> hello@crestmoorvalor.com</p>
      <p class="web">www.<span class="domain">crestmoorvalor</span>.com</p>
      <p>PO BOX 417 Ashdale Road, 2nd street, Melbourne</p>
    </div>

    <div class="base-band"></div>
  </section>
</div>
</body>
</html>
```